Birchlane Chiropractic Business Cards

Business cards with new logo design. Will upload copy of current card. We like the layout, but we need a new logo. Family, husband holding up baby toward sky, mom and other child standing next to him. We will probably want to include a catch phrase with logo. TBD

```html
<!DOCTYPE html>
<html lang="en">
<head>
<meta charset="utf-8">
<title>Birchlane Chiropractic Business Cards</title>
<link rel="stylesheet" href="https://fonts.googleapis.com/css2?family=Open+Sans:wght@400;700;800&display=swap">
<style>
  :root {
    --brand-blue: #22408f;
    --brand-red: #e3262d;
    --card-white: #f7f7f7;
    --ink: #1f1f24;
    --page: #e9e9ec;
  }
  * { box-sizing: border-box; margin: 0; padding: 0; }
  html, body { width: 1200px; height: 900px; overflow: hidden; }
  body {
    background: var(--page);
    font-family: "Open Sans", sans-serif;
    position: relative;
  }
  .card {
    position: absolute;
    left: 240px;
    width: 720px;
    height: 411px;
    overflow: hidden;
    box-shadow: 0 6px 18px rgba(0,0,0,.18);
  }
  /* Back of card */
  .card--back { top: 22px; background: var(--brand-blue); }
  .back-band {
    position: absolute;
    left: 0; right: 0;
    top: 292px;
    height: 52px;
    background: var(--brand-red);
    display: flex;
    align-items: center;
    justify-content: center;
  }
  .back-band__name {
    color: #ffffff;
    font-weight: 800;
    font-size: 30px;
    letter-spacing: 3px;
    text-transform: uppercase;
  }
  /* Front of card */
  .card--front {
    top: 466px;
    background: var(--brand-blue);
    padding: 12px;
  }
  .front-panel {
    position: relative;
    width: 100%;
    height: 100%;
    background: var(--card-white);
    overflow: hidden;
  }
  .front-wave { position: absolute; left: 0; bottom: 0; width: 696px; height: 387px; }
  .brand {
    position: absolute;
    left: 24px;
    top: 150px;
    width: 280px;
    display: flex;
    align-items: center;
    gap: 10px;
  }
  .brand__mark {
    width: 16px; height: 16px;
    border-radius: 50%;
    background: var(--brand-blue);
    flex: none;
  }
  .brand__name {
    color: var(--brand-blue);
    font-weight: 800;
    font-size: 21px;
    line-height: 1.15;
    text-transform: uppercase;
    letter-spacing: .5px;
  }
  .divider {
    position: absolute;
    left: 322px;
    top: 62px;
    width: 2px;
    height: 210px;
    background: var(--brand-blue);
  }
  .details { position: absolute; left: 342px; top: 58px; right: 16px; }
  .details__name {
    color: var(--brand-blue);
    font-weight: 700;
    font-size: 27px;
    line-height: 1.1;
  }
  .details__title {
    color: var(--ink);
    font-size: 16px;
    margin-bottom: 18px;
  }
  .contact {
    list-style: none;
    color: var(--ink);
    font-size: 16px;
  }
  .contact li { display: flex; align-items: flex-start; gap: 12px; margin-bottom: 6px; line-height: 1.3; }
  .contact svg { width: 18px; height: 18px; flex: none; margin-top: 2px; }
</style>
</head>
<body>

<section class="card card--back" aria-label="Card back">
  <div class="back-band">
    <span class="back-band__name">Birchlane Chiropractic</span>
  </div>
</section>

<section class="card card--front" aria-label="Card front">
  <div class="front-panel">
    <svg class="front-wave" viewBox="0 0 696 387" preserveAspectRatio="none" aria-hidden="true">
      <path d="M0 312 C 150 296, 260 300, 400 330 S 600 372, 696 360 L696 387 L0 387 Z" fill="var(--brand-blue)"/>
      <path d="M0 300 C 150 284, 260 290, 400 318 S 600 352, 696 344 L696 350 C 600 358, 500 344, 400 326 S 150 292, 0 308 Z" fill="var(--brand-red)"/>
    </svg>

    <div class="brand">
      <span class="brand__mark"></span>
      <span class="brand__name">Birchlane<br>Chiropractic</span>
    </div>

    <div class="divider"></div>

    <div class="details">
      <h1 class="details__name">Dr.Daniel R.Ostrow</h1>
      <p class="details__title">Chiropractic Physician</p>
      <ul class="contact">
        <li>
          <svg viewBox="0 0 24 24" fill="none" stroke="var(--brand-blue)" stroke-width="2"><path d="M5 3h4l2 5-3 2a12 12 0 0 0 6 6l2-3 5 2v4a2 2 0 0 1-2 2A18 18 0 0 1 3 5a2 2 0 0 1 2-2z"/></svg>
          <span>503 555 0142</span>
        </li>
        <li>
          <svg viewBox="0 0 24 24" fill="none" stroke="var(--brand-blue)" stroke-width="2"><rect x="6" y="3" width="12" height="6"/><rect x="3" y="9" width="18" height="8"/><rect x="7" y="14" width="10" height="7"/></svg>
          <span>503 555 0199</span>
        </li>
        <li>
          <svg viewBox="0 0 24 24" fill="none" stroke="var(--brand-blue)" stroke-width="1.6"><circle cx="12" cy="12" r="9"/><ellipse cx="12" cy="12" rx="4" ry="9"/><path d="M3 12h18M5 7h14M5 17h14"/></svg>
          <span>www.birchlanechiro.com</span>
        </li>
        <li>
          <svg viewBox="0 0 24 24" fill="var(--brand-blue)"><path d="M12 2a7 7 0 0 0-7 7c0 5 7 13 7 13s7-8 7-13a7 7 0 0 0-7-7zm0 9.5A2.5 2.5 0 1 1 12 6.5a2.5 2.5 0 0 1 0 5z"/></svg>
          <span>2240 SE Cedar Ridge Town Center<br>Dr.Fernwood,Oregon 97000</span>
        </li>
      </ul>
    </div>
  </div>
</section>

</body>
</html>
```